Downloadable PDF "Brochure?"

We have a Free download we will provide in exchange for an email address on our new Trailmark website. The website at www.venturetrailmark-example.com is in development and will look nothing like what it currently does, but you can go there and get a sense of what Trailmark is from the text on the website. (see the attached image 'site design' for the new redesigned website for aesthetics).

We are looking for a nice design for the document, that will represent the mostly text document well. We are not actually looking to print these at a printer so they don't have to be print ready. I went ahead and included the logo and colors and fonts file again just for reference.

Target Market(s)

Business Owners / Decision Makers

Requirements
Must have
• See attached document 'trailmark freebie' for text to be utilized in the finished deliverable.
• See the attached image 'Site Design' for the website aesthetic.

```html
<!DOCTYPE html>
<html lang="en">
<head>
<meta charset="utf-8">
<title>Trailmark – 10 Questions To Choose The Best Technology Advisor</title>
<link href="https://fonts.googleapis.com/css2?family=Open+Sans:wght@400;600&family=Oswald:wght@300;400;600&display=swap" rel="stylesheet">
<style>
  :root{
    --ink:#2f3e46;
    --ink-deep:#253238;
    --copper:#c9743f;
    --copper-light:#e0804a;
    --heading:#c8713d;
    --text:#4a4a4a;
    --paper:#ffffff;
  }
  *{margin:0;padding:0;box-sizing:border-box}
  html,body{width:938px;height:1200px;overflow:hidden;background:var(--paper)}
  .page{position:relative;width:938px;height:1200px;overflow:hidden;background:var(--paper);font-family:"Open Sans",sans-serif;color:var(--text)}
  .shapes{position:absolute;inset:0}
  .brand{position:absolute;left:212px;top:138px;width:320px;text-align:center;color:var(--ink)}
  .brand__name{font-family:"Open Sans",sans-serif;font-weight:600;font-size:30px;letter-spacing:3px;line-height:1}
  .brand__tagline{font-family:"Open Sans",sans-serif;font-weight:600;font-size:12px;letter-spacing:1.5px;margin-top:8px;text-transform:uppercase}
  .title{position:absolute;right:34px;top:30px;text-align:right;font-family:"Oswald",sans-serif;line-height:1}
  .title__number{font-weight:600;font-size:92px;color:var(--copper-light);letter-spacing:-3px}
  .title__word{font-weight:600;font-size:42px;color:var(--copper-light);margin-top:2px}
  .title__sub{font-weight:300;font-size:31px;color:#fff;line-height:36px;margin-top:4px}
  .intro{position:absolute;left:112px;top:570px;width:763px;height:83px;padding:7px 18px 0 17px;font-size:13.5px;letter-spacing:0.2px;line-height:15.5px}
  .intro::before,.intro::after{content:"";position:absolute;top:0;bottom:0;width:28px;border:1.5px solid var(--copper)}
  .intro::before{left:0;border-right:none}
  .intro::after{right:0;border-left:none}
  .intro-rule{position:absolute;top:613px;height:1.5px;background:var(--copper)}
  .question{position:absolute;left:44px;width:850px}
  .question__icon{position:absolute;left:0;width:65px;height:59px;background:var(--ink);border-right:12px solid #3b4a52}
  .question__icon svg{position:absolute;left:9px;top:9px}
  .question__head{margin-left:80px;color:var(--heading);font-weight:600;font-size:18px;letter-spacing:0.2px;line-height:20px;text-transform:uppercase;white-space:nowrap}
  .question__body{font-size:13.5px;letter-spacing:0.2px;line-height:15.5px;margin-top:20px}
  .placeholder{position:absolute}
  .footer-url{position:absolute;left:55px;top:1173px;display:flex;align-items:center;gap:7px;color:#fff;font-size:13.5px;text-transform:uppercase}
</style>
</head>
<body>
<div class="page">
  <svg class="shapes" width="938" height="1200" viewBox="0 0 938 1200">
    <defs>
      <linearGradient id="ink-grad" x1="0" y1="0" x2="1" y2="1">
        <stop offset="0" stop-color="#3d4c54"/><stop offset="1" stop-color="#263238"/>
      </linearGradient>
      <linearGradient id="copper-grad" x1="0" y1="0" x2="1" y2="0">
        <stop offset="0" stop-color="#e3804a"/><stop offset="1" stop-color="#b96d3f"/>
      </linearGradient>
      <linearGradient id="people-grad" x1="0" y1="0" x2="1" y2="1">
        <stop offset="0" stop-color="#6f7479"/><stop offset="0.6" stop-color="#3a3e44"/><stop offset="1" stop-color="#d9dadb"/>
      </linearGradient>
      <linearGradient id="puzzle-grad" x1="0" y1="0" x2="1" y2="1">
        <stop offset="0" stop-color="#5a5a6a"/><stop offset="0.5" stop-color="#c9c9cc"/><stop offset="0.75" stop-color="#b8242a"/><stop offset="1" stop-color="#3a3a48"/>
      </linearGradient>
      <linearGradient id="qa-grad" x1="0" y1="0" x2="1" y2="0">
        <stop offset="0" stop-color="#c7302c"/><stop offset="0.45" stop-color="#d4a52a"/><stop offset="1" stop-color="#4b9a3a"/>
      </linearGradient>
    </defs>
    <polygon points="0,0 170,151 0,303" fill="url(#ink-grad)"/>
    <polygon points="0,358 167,509 0,659" fill="url(#copper-grad)"/>
    <polygon points="604,0 727,0 533,175 471,116" fill="url(#copper-grad)"/>
    <polygon points="756,0 938,0 938,458 594,151" fill="url(#ink-grad)"/>
    <polygon points="579,163 762,327 579,493 396,327" fill="url(#ink-grad)"/>
    <polygon points="717,1200 938,1200 938,1166 0,1166 0,1200" fill="url(#copper-grad)"/>
    <polygon points="649,1200 707,1148 765,1200" fill="var(--ink)"/>
    <polygon points="808,1051 898,1131 820,1200 720,1131" fill="var(--ink)"/>
    <polygon points="938,1120 938,1200 848,1200" fill="var(--copper-light)"/>
  </svg>

  <svg class="placeholder" style="left:0;top:0" width="938" height="560" viewBox="0 0 938 560">
    <polygon role="img" aria-label="Photo of two businessmen discussing over a tablet" points="10,420 10,300 120,225 240,225 365,330 260,440" fill="url(#people-grad)"/>
    <polygon role="img" aria-label="Photo of a team assembling puzzle pieces on a table" points="579,172 752,327 579,482 406,327" fill="url(#puzzle-grad)"/>
    <rect role="img" aria-label="Illustration of a figure reading on large Q and A letters" x="281" y="400" width="182" height="136" rx="6" fill="url(#qa-grad)" opacity="0.85"/>
  </svg>

  <div class="brand">
    <div class="brand__name">TRAILMARK</div>
    <div class="brand__tagline">Chart your next course</div>
  </div>

  <div class="title">
    <div class="title__number">10</div>
    <div class="title__word">QUESTIONS</div>
    <div class="title__sub">To Choose The<br>Best Technology<br>Advisor</div>
  </div>

  <div class="intro-rule" style="left:51px;width:50px"></div>
  <div class="intro-rule" style="left:887px;width:51px"></div>
  <p class="intro">When you choose a technology advisor whether it be a Managed Service Provider, fractional CIO or a full-time CIO you need to make sure that they understand business just as much as they understand technology. Some of the biggest complaints about the IT department are that they just don’t “Get it”. The questions below should help you determine whether or not they have a technology mindset or a business mindset.</p>

  <section class="question" style="top:713px">
    <div class="question__icon">
      <svg width="36" height="40" viewBox="0 0 36 40" fill="none" stroke="#fff" stroke-width="2.5">
        <rect x="10" y="4" width="22" height="22" stroke-dasharray="4 3"/>
        <rect x="3" y="20" width="15" height="15" fill="#fff"/>
        <path d="M15 21 L26 10 M19 10 H26 V17"/>
      </svg>
    </div>
    <h2 class="question__head">What is scalability?<br>How important is it from a technology perspective on a scale of 1-&gt;10<br>with 10 being the highest? What all does scalability impact?</h2>
    <p class="question__body">This question is designed to get a reading on the person’s mindset. A typical technology-minded response would be something describing the ability of systems or software to scale by adding additional resources. When working from a business point of view, however, you want to see it defined as the ability for the organization to support increased volume without sacrificing margins. The importance of this concept cannot be overstated and should be a 9 or 10 in terms of ranking. Regarding impact, you want to see not just an understanding of having to spend money two or three times for a different solution to the same problem, but an acknowledgment of the ‘total’ cost, including adoption fatigue, the opportunity cost of change, and the competitive disadvantage it creates. For concepts of business scalability refer to ‘Growing Steady’ by Dale Corrigan.</p>
  </section>

  <section class="question" style="top:919px">
    <div class="question__icon">
      <svg width="36" height="40" viewBox="0 0 36 40" fill="none" stroke="#fff" stroke-width="2">
        <rect x="6" y="10" width="24" height="20"/>
        <path d="M18 30 V36 M11 36 H25 M12 10 V4 M18 10 V2 M24 10 V4 M12 16 V24 M18 14 V26 M24 16 V24"/>
        <circle cx="12" cy="3" r="1.5"/><circle cx="24" cy="3" r="1.5"/>
      </svg>
    </div>
    <h2 class="question__head" style="padding-top:18px">Provide an example where you solved a problem without<br>the use of technology.</h2>
    <p class="question__body">Often technology-minded individuals become so wrapped up in the solutions themselves they fail to realize a policy or process change is far more effective and simple than making changes to existing or introducing new technology. Asking for a specific example here should demonstrate the ability to think from a business mindset. For specific examples reference<br>‘The Lantern Workshop’ by Ames, Rolle, and Tennant.</p>
  </section>

  <div class="footer-url">
    <svg width="20" height="20" viewBox="0 0 20 20" fill="none" stroke="#fff" stroke-width="1.2">
      <circle cx="10" cy="10" r="8.5"/><ellipse cx="10" cy="10" rx="4" ry="8.5"/><path d="M1.5 10 H18.5 M3 5.5 H17 M3 14.5 H17"/>
    </svg>
    <span>www.venturetrailmark-example.com</span>
  </div>
</div>
</body>
</html>
```